Trade show Banner to be displayed on vertical stand

We are an IT company that specializes in working with Manufacturing companies and manufacturing plants. We need two banners designed for a manufacturing trade show. The design needs to be designed using the supplied template file. Also the design needs to communicate graphically that we specialize in working with manufacturing plants. Also they should communicate that out services include: IT Services, Network, Voice, Data

Target Market(s)

Manufacturing companies

Industry/Entity Type

Manufacturing

Requirements
Must have
• Clear message, clear graphic message. Must be designed with included templates
Nice to have
• Company colors need to be used, but additional colors can be used

```html
<!DOCTYPE html>
<html lang="en">
<head>
<meta charset="utf-8">
<title>Gridline Works – Trade Show Banners</title>
<link rel="stylesheet" href="https://fonts.googleapis.com/css2?family=Fira+Sans+Extra+Condensed:wght@700;800&family=Montserrat:wght@400;500;700;800&display=swap">
<style>
  :root {
    --brand-blue: #2b72be;
    --brand-blue-deep: #1f5e9f;
    --ink: #0d0d0f;
    --steel: #8b8d91;
    --paper: #eef0f2;
    --stage: #e3e4e6;
    --white: #ffffff;
  }
  * { box-sizing: border-box; margin: 0; padding: 0; }
  html, body { width: 1200px; height: 1200px; overflow: hidden; }
  body { background: var(--stage); font-family: "Montserrat", sans-serif; position: relative; }

  .banner {
    position: absolute; top: 100px; width: 400px; height: 1000px;
    background: var(--paper); overflow: hidden;
    box-shadow: 0 18px 40px rgba(0,0,0,.12);
  }
  .banner--industry { left: 150px; }
  .banner--services { left: 650px; }
  .banner-art { position: absolute; inset: 0; width: 400px; height: 1000px; }

  .brand {
    position: absolute; top: 70px; left: 44px;
    display: flex; align-items: center; gap: 14px;
  }
  .brand-dot { width: 54px; height: 54px; border-radius: 50%; background: var(--brand-blue); flex: none; }
  .brand-name {
    font-family: "Montserrat", sans-serif; font-weight: 700; font-size: 30px;
    color: var(--brand-blue); letter-spacing: .5px; white-space: nowrap;
  }
  .banner--services .brand { top: 60px; }

  .headline {
    position: absolute; left: 52px; top: 700px; width: 320px;
    color: var(--white); transform: rotate(-6deg); transform-origin: left top;
    line-height: 1; white-space: nowrap;
  }
  .headline-strong {
    display: block; font-family: "Fira Sans Extra Condensed", sans-serif;
    font-weight: 800; font-size: 42px; letter-spacing: .3px;
  }
  .headline-light { display: block; font-weight: 400; font-size: 27px; margin: 4px 0 6px 26px; }
  .headline-big { display: block; font-weight: 800; font-size: 62px; letter-spacing: 1px; margin-top: 6px; }

  .service-list {
    position: absolute; left: 50px; top: 640px; width: 330px; list-style: none;
    transform: rotate(4deg); transform-origin: left top;
  }
  .service-item { display: flex; align-items: center; height: 50px; }
  .service-icon {
    width: 42px; height: 42px; border-radius: 50%; background: var(--white);
    display: flex; align-items: center; justify-content: center; flex: none;
    box-shadow: 0 3px 6px rgba(0,0,0,.25);
  }
  .service-rule { width: 2px; height: 36px; background: var(--white); margin: 0 20px 0 24px; opacity: .9; }
  .service-label { color: var(--white); font-weight: 800; font-size: 29px; letter-spacing: .5px; white-space: nowrap; }

  .site-url {
    position: absolute; color: var(--white); font-size: 24px; font-weight: 500;
    white-space: nowrap; letter-spacing: .5px;
  }
  .site-url strong { font-weight: 800; }
  .banner--industry .site-url { left: 95px; top: 930px; transform: rotate(-7deg); }
  .banner--services .site-url { left: 85px; top: 912px; transform: rotate(5deg); }
</style>
</head>
<body>

<section class="banner banner--industry" aria-label="Manufacturing specialty banner">
  <svg class="banner-art" viewBox="0 0 400 1000">
    <defs>
      <linearGradient id="robotArmTone" x1="0" y1="0" x2="1" y2="1">
        <stop offset="0" stop-color="#c9d6e4"/>
        <stop offset=".5" stop-color="#8e9fb3"/>
        <stop offset="1" stop-color="#4d5a6a"/>
      </linearGradient>
    </defs>
    <polygon points="0,250 400,175 400,1000 0,1000" fill="var(--brand-blue)"/>
    <polygon points="160,265 400,205 400,290" fill="var(--ink)"/>
    <g role="img" aria-label="Photo of a robotic gripper arm on a factory production line">
      <polygon points="0,290 400,235 400,520 0,575" fill="url(#robotArmTone)"/>
    </g>
    <polygon points="0,575 400,520 400,560 0,670" fill="var(--ink)"/>
    <polygon points="0,575 260,545 0,660" fill="var(--steel)"/>
    <polygon points="0,930 400,865 400,1000 0,1000" fill="var(--ink)"/>
  </svg>

  <div class="brand">
    <span class="brand-dot"></span>
    <span class="brand-name">Gridline Works</span>
  </div>

  <h1 class="headline">
    <span class="headline-strong">WE SPECIALIZE IN</span>
    <span class="headline-light">WORKING WITH</span>
    <span class="headline-strong">MANUFACTURING</span>
    <span class="headline-big">PLANTS</span>
  </h1>

  <p class="site-url">www.<strong>gridlineit</strong>.com</p>
</section>

<section class="banner banner--services" aria-label="Services banner">
  <svg class="banner-art" viewBox="0 0 400 1000">
    <defs>
      <linearGradient id="operatorTone" x1="0" y1="0" x2="1" y2="1">
        <stop offset="0" stop-color="#b7c8da"/>
        <stop offset=".55" stop-color="#6f86a0"/>
        <stop offset="1" stop-color="#34465c"/>
      </linearGradient>
    </defs>
    <polygon points="0,255 400,170 400,1000 0,1000" fill="var(--brand-blue)"/>
    <polygon points="180,250 400,195 400,260" fill="var(--ink)"/>
    <g role="img" aria-label="Photo of a factory worker operating a machine control panel">
      <polygon points="0,300 400,235 400,560 0,550" fill="url(#operatorTone)"/>
    </g>
    <polygon points="0,550 400,560 400,595 0,620" fill="var(--ink)"/>
    <polygon points="0,550 220,575 0,612" fill="var(--steel)"/>
    <polygon points="0,860 400,935 400,1000 0,1000" fill="var(--ink)"/>
  </svg>

  <div class="brand">
    <span class="brand-dot"></span>
    <span class="brand-name">Gridline Works</span>
  </div>

  <ul class="service-list">
    <li class="service-item">
      <span class="service-icon">
        <svg width="26" height="26" viewBox="0 0 28 28" fill="none" stroke="#2b72be" stroke-width="1.8">
          <circle cx="14" cy="14" r="10"/><ellipse cx="14" cy="14" rx="4.5" ry="10"/><line x1="4" y1="14" x2="24" y2="14"/>
        </svg>
      </span>
      <span class="service-rule"></span>
      <span class="service-label">IT SERVICES</span>
    </li>
    <li class="service-item">
      <span class="service-icon">
        <svg width="26" height="26" viewBox="0 0 28 28" fill="none" stroke="#2b72be" stroke-width="1.8">
          <circle cx="14" cy="14" r="3"/><circle cx="5" cy="5" r="2.5"/><circle cx="23" cy="5" r="2.5"/><circle cx="5" cy="23" r="2.5"/><circle cx="23" cy="23" r="2.5"/>
          <path d="M7 7l5 5M21 7l-5 5M7 21l5-5M21 21l-5-5"/>
        </svg>
      </span>
      <span class="service-rule"></span>
      <span class="service-label">NETWORK</span>
    </li>
    <li class="service-item">
      <span class="service-icon">
        <svg width="26" height="26" viewBox="0 0 28 28" fill="none" stroke="#2b72be" stroke-width="1.8">
          <rect x="10" y="3" width="8" height="14" rx="4"/><path d="M6 13a8 8 0 0 0 16 0M14 21v5M10 26h8"/>
        </svg>
      </span>
      <span class="service-rule"></span>
      <span class="service-label">VOICE</span>
    </li>
    <li class="service-item">
      <span class="service-icon">
        <svg width="26" height="26" viewBox="0 0 28 28" fill="none" stroke="#2b72be" stroke-width="1.8">
          <ellipse cx="14" cy="6" rx="9" ry="3"/><path d="M5 6v16c0 1.7 4 3 9 3s9-1.3 9-3V6M5 14c0 1.7 4 3 9 3s9-1.3 9-3"/>
        </svg>
      </span>
      <span class="service-rule"></span>
      <span class="service-label">DATA</span>
    </li>
  </ul>

  <p class="site-url">www.<strong>gridlineit</strong>.com</p>
</section>

</body>
</html>
```